hi all

Im after a new age looking business card with my company logo on it

must include these details, I would like the PH and Email to be symbols

If the colours used for card could be kept within the colours used in logo that I have supplied that would be great, if another colour is to be used dark grey would be ok. no light bulbs etc thanks

Details below to be incorporated on card

Damian Holloway

Lic E871302

PH 0219647381

E info@brightvaleelectrical.example.nz

Domestic Commercial Industrial Electricians

```html
<!DOCTYPE html>
<html lang="en">
<head>
<meta charset="utf-8">
<title>Brightvale Electrical – Business Card</title>
<link href="https://fonts.googleapis.com/css2?family=Lato:wght@400;700;900&display=swap" rel="stylesheet">
<style>
  :root {
    --backdrop: #3a332f;
    --card: #161619;
    --card-edge: #1f7fd4;
    --brand-blue: #1f7fd4;
    --text-light: #f2f2f2;
    --text-muted: #d6d6d6;
    --decor: #222226;
  }
  * { margin: 0; padding: 0; box-sizing: border-box; }
  html, body { width: 1200px; height: 847px; overflow: hidden; }
  body {
    background: var(--backdrop);
    font-family: "Lato", Arial, sans-serif;
    position: relative;
  }
  .card {
    position: absolute;
    width: 520px;
    height: 300px;
    background: var(--card);
    border-bottom: 5px solid var(--card-edge);
    overflow: hidden;
    box-shadow: 0 10px 30px rgba(0,0,0,.45);
  }
  .card--front { left: 50px; top: 110px; }
  .card--back { left: 630px; top: 420px; }

  .decor-circle {
    position: absolute;
    border-radius: 50%;
    background: var(--decor);
  }
  .card--front .decor-circle { width: 260px; height: 260px; left: 40px; top: -30px; }
  .card--back .decor-circle { width: 170px; height: 170px; right: 30px; top: 90px; }

  .wordmark {
    position: absolute;
    color: var(--brand-blue);
    font-weight: 900;
    text-transform: uppercase;
    line-height: 1;
    letter-spacing: 1px;
    text-align: right;
  }
  .card--front .wordmark { right: 30px; bottom: 40px; font-size: 34px; }
  .card--front .wordmark span { display: block; font-size: 34px; }

  .card--back .brand {
    position: absolute;
    left: 0; right: 0; top: 24px;
    display: flex; flex-direction: column; align-items: center; gap: 8px;
  }
  .brand-dot {
    width: 38px; height: 38px; border-radius: 50%;
    border: 3px solid var(--text-light);
  }
  .card--back .wordmark { position: static; font-size: 26px; text-align: center; }

  .person {
    position: absolute; left: 36px; top: 128px;
    font-size: 26px; font-weight: 700; color: var(--text-light);
  }
  .person .first { color: var(--brand-blue); }

  .contact { position: absolute; left: 36px; top: 168px; list-style: none; }
  .contact li {
    display: flex; align-items: center; gap: 10px;
    font-size: 15px; color: var(--text-muted); margin-bottom: 6px;
  }
  .contact svg { width: 15px; height: 15px; fill: var(--brand-blue); flex: none; }

  .rule {
    position: absolute; left: 36px; right: 36px; top: 234px;
    height: 1px; background: var(--brand-blue);
  }
  .services {
    position: absolute; left: 36px; top: 245px;
    font-size: 14px; color: var(--text-muted);
  }
  .licence {
    position: absolute; right: 36px; top: 242px;
    font-size: 20px; color: var(--text-light);
  }
</style>
</head>
<body>

  <section class="card card--front" aria-label="Card front">
    <div class="decor-circle" aria-hidden="true"></div>
    <div class="wordmark">Brightvale<span>Electrical</span></div>
  </section>

  <section class="card card--back" aria-label="Card back">
    <div class="decor-circle" aria-hidden="true"></div>
    <div class="brand">
      <div class="brand-dot" aria-hidden="true"></div>
      <div class="wordmark">Brightvale Electrical</div>
    </div>

    <p class="person"><span class="first">Damian</span> Holloway</p>

    <ul class="contact">
      <li>
        <svg viewBox="0 0 24 24" aria-hidden="true"><path d="M6.6 10.8a15.2 15.2 0 0 0 6.6 6.6l2.2-2.2a1 1 0 0 1 1-.25 11.4 11.4 0 0 0 3.6.57 1 1 0 0 1 1 1V20a1 1 0 0 1-1 1A17 17 0 0 1 3 4a1 1 0 0 1 1-1h3.5a1 1 0 0 1 1 1c0 1.25.2 2.45.57 3.57a1 1 0 0 1-.25 1z"/></svg>
        021 964 7381
      </li>
      <li>
        <svg viewBox="0 0 24 24" aria-hidden="true"><path d="M2 5h20v14H2z M4 7v.3l8 5.2 8-5.2V7z" fill-rule="evenodd"/></svg>
        info@brightvaleelectrical.example.nz
      </li>
    </ul>

    <div class="rule" aria-hidden="true"></div>
    <p class="services">Domestic Commercial Industrial Electricians</p>
    <p class="licence">Lic E871302</p>
  </section>

</body>
</html>
```